Kettle Ledger Business Card design

We need a stand out business card design for Accounting practice based in Australia specialising in pubs, clubs and hotels. We help venues maximise margins, create time and manage cashflow. One club we have been working with for the last 6 months has increased revenue by 3% and margin by 5% in this time frame. We have a back office outsourced system that costs less than having a full time employee and also allows the venues the added benefit of:<br/>-using the office space to become a revenue generating opportunity. <br/>-a complete system to enhance governance, accountability and efficiency within their operation<br/>-52 weeks cover so no hassle to cover annual/sick .. leave<br/><br/>We would like to see designs that use the colours of our logo (green & blue).
Target Market(s)
Australian Pubs, Clubs & Hotels abookkeeping, accounting and tax services
Industry/Entity Type
Accountant
Contact Information for Business Card
Miriam Oakley CPA
Principal
Accountant Tax Agent
Miriam@KettleLedger-example.com.au
0418693142
www.kettleledger-example.com.au
Accounting / Payroll / Tax / SMSF / Technology
Colors
Designer to choose colors to be used in the design.
Look and feel
Each slider illustrates characteristics of the customer's brand and the style your logo design should communicate.

```html
<!DOCTYPE html>
<html lang="en">
<head>
<meta charset="utf-8">
<title>Kettle Ledger Business Card</title>
<link href="https://fonts.googleapis.com/css2?family=Arimo:wght@400;700&display=swap" rel="stylesheet">
<style>
  :root {
    --stage: #2a2a2a;
    --card: #f7f7f6;
    --brand-blue: #1f3f95;
    --brand-green: #1e6b3a;
    --hop-green: #7fb3a0;
    --ink: #2b2b2b;
    --icon-navy: #1f3a6e;
    --badge-gold: #f2c830;
    --badge-sky: #2c6fb5;
    --badge-lime: #c9d84a;
    --badge-black: #161616;
  }
  * { margin: 0; padding: 0; box-sizing: border-box; }
  html, body { width: 1200px; height: 997px; overflow: hidden; }
  body {
    background: var(--stage);
    font-family: "Arimo", Arial, sans-serif;
    position: relative;
  }
  .card {
    position: absolute;
    width: 560px;
    height: 320px;
    background: var(--card);
    box-shadow: 0 10px 30px rgba(0,0,0,.5);
    overflow: hidden;
  }
  .card--front { left: 90px; top: 130px; }
  .card--back { left: 550px; top: 530px; }

  .front-brand {
    position: absolute;
    left: 0; right: 0; top: 105px;
    text-align: center;
    font-size: 52px;
    font-weight: 700;
    color: var(--brand-blue);
    letter-spacing: -1px;
  }
  .badges {
    position: absolute;
    left: 0; right: 0; top: 205px;
    display: flex;
    justify-content: center;
    align-items: center;
    gap: 16px;
  }
  .badge { display: block; }
  .badge--member { width: 62px; height: 30px; background: var(--badge-gold); border: 3px solid var(--badge-sky); }
  .badge--registered { width: 40px; height: 40px; border-radius: 50%; background: var(--badge-lime); border: 3px solid #e8e8e8; }
  .badge--listing { width: 30px; height: 30px; background: var(--badge-black); }

  .back-brand {
    position: absolute;
    left: 36px; top: 60px;
    font-size: 46px;
    font-weight: 700;
    color: var(--brand-blue);
    letter-spacing: -1px;
  }
  .back-accent {
    position: absolute;
    right: -70px; top: -40px;
    width: 320px; height: 320px;
    border-radius: 50%;
    background: var(--hop-green);
    opacity: .18;
  }
  .contact {
    position: absolute;
    left: 36px; top: 188px;
  }
  .contact__name {
    font-size: 17px;
    font-weight: 700;
    color: var(--brand-green);
    letter-spacing: .3px;
  }
  .contact__role {
    font-size: 14px;
    color: var(--brand-blue);
    line-height: 1.15;
    margin-top: 4px;
  }
  .contact__list { list-style: none; margin-top: 10px; }
  .contact__item {
    display: flex;
    align-items: center;
    gap: 10px;
    font-size: 17px;
    color: var(--ink);
    margin-bottom: 6px;
  }
  .contact__icon { width: 18px; height: 18px; flex: none; }
</style>
</head>
<body>
  <section class="card card--front" aria-label="Card front">
    <div class="front-brand">Kettle Ledger</div>
    <div class="badges">
      <span class="badge badge--member" role="img" aria-label="Professional membership badge"></span>
      <span class="badge badge--registered" role="img" aria-label="Registered tax agent badge"></span>
      <span class="badge badge--listing" role="img" aria-label="Directory listing badge"></span>
    </div>
  </section>

  <section class="card card--back" aria-label="Card back">
    <div class="back-accent" aria-hidden="true"></div>
    <div class="back-brand">Kettle Ledger</div>
    <div class="contact">
      <p class="contact__name">MIRIAM OAKLEY CPA</p>
      <p class="contact__role">Principal<br>Accountant Tax Agent</p>
      <ul class="contact__list">
        <li class="contact__item">
          <svg class="contact__icon" viewBox="0 0 18 18" aria-hidden="true">
            <circle cx="9" cy="9" r="9" fill="var(--icon-navy)"/>
            <path d="M5 7.5c0-1.5 1.8-2.5 4-2.5s4 1 4 2.5l-1.6.6-.6-1.3H7.2l-.6 1.3zM5.5 9h7l.5 4H5z" fill="#fff"/>
          </svg>
          0418693142
        </li>
        <li class="contact__item">
          <svg class="contact__icon" viewBox="0 0 18 18" aria-hidden="true">
            <circle cx="9" cy="9" r="9" fill="var(--icon-navy)"/>
            <rect x="4.5" y="6" width="9" height="6.5" fill="none" stroke="#fff" stroke-width="1.2"/>
            <path d="M4.5 6l4.5 3.8L13.5 6" fill="none" stroke="#fff" stroke-width="1.2"/>
          </svg>
          miriam@kettleledger-example.com.au
        </li>
      </ul>
    </div>
  </section>
</body>
</html>
```